Coldforge Prime manufacturing Project

We are looking at getting a brand new design for a new company that deals in selling stainless tubing and other stainless still products such as handrails, Spigots, Balustrade Fittings
Glass, Glass fittings and Aluminium Channels

We require a very clean website that deals with the following colours:

Blue to light blues
Blacks
Greys to light Greys
Whites

We are open for other ideas BUT we *DO NOT* want any pinks, greens or bright colours except for backgrounds colours we have chosen above. (It can be solid, gradient or a subtle pattern)

YOU MUST KEEP THE LOGO AS IS. PLEASE DO NOT ALTER THE LOGO IN *ANY WAY* and the logo MUST be the same colours and fonts.

Logo is attached.

The site must contain these aspects:
jQuery Slider (Image slide show)
Top drop down Menus
Be no more than 900px wide
Text is to be to the w3C standards. (no special fonts)

We will chop up the design into html format. You just need to provide the PSD file.

The clients opposition is:
www.quorvatrim.example

Industry/Entity Type

It Company

Requirements
Nice to have
• Alter the logo in anyway

Files

```html
<!DOCTYPE html>
<html lang="en">
<head>
<meta charset="utf-8">
<title>Coldforge Prime – Stainless Railing Systems</title>
<link rel="stylesheet" href="https://fonts.googleapis.com/css2?family=PT+Sans:wght@400;700&display=swap">
<style>
  :root {
    --blue: #396497;
    --blue-dark: #2f5888;
    --blue-menu: #3d6a9e;
    --black: #0a0a0a;
    --grey: #9b9b9b;
    --grey-dark: #6b6b6b;
    --grey-text: #7a7a7a;
    --white: #ffffff;
  }
  * { margin: 0; padding: 0; box-sizing: border-box; }
  html, body { width: 850px; height: 1200px; overflow: hidden; background: var(--white); }
  body { font-family: "PT Sans", Arial, sans-serif; color: var(--white); position: relative; }
  .abs { position: absolute; }

  .textured-blue {
    background-color: var(--blue);
    background-image: repeating-linear-gradient(135deg, rgba(255,255,255,0.04) 0 1px, transparent 1px 3px);
  }
  .textured-grey {
    background-color: var(--grey);
    background-image: repeating-linear-gradient(135deg, rgba(255,255,255,0.05) 0 1px, transparent 1px 3px);
  }

  /* Header */
  .site-header { left: 0; top: 0; width: 850px; height: 155px; border-top: 6px solid #5a80ad; }
  .brand { left: 31px; top: 40px; display: flex; align-items: center; gap: 12px; }
  .brand-mark { width: 94px; height: 94px; border-radius: 50%; background: #1c1c1c; border: 4px solid #cfd6de; }
  .brand-name { font-size: 19px; font-weight: 400; color: var(--white); }
  .main-nav { left: 394px; top: 86px; display: flex; font-size: 15px; font-weight: 700; }
  .main-nav a { color: var(--white); text-decoration: none; position: absolute; white-space: nowrap; }

  .dropdown { left: 524px; top: 115px; width: 173px; background: var(--blue-menu);
    box-shadow: 0 2px 4px rgba(0,0,0,0.45); z-index: 5; }
  .dropdown li { list-style: none; height: 32.7px; line-height: 32px; text-align: center; font-size: 14px;
    letter-spacing: 0.3px; border-bottom: 1px solid rgba(20,40,70,0.45); border-top: 1px solid rgba(255,255,255,0.08); }

  /* Utility bar */
  .utility-bar { left: 0; top: 155px; width: 850px; height: 24px; background: var(--black); }
  .utility-link { left: 395px; top: 4px; font-size: 12px; color: var(--white); }
  .search-field { left: 694px; top: 6px; width: 78px; height: 12px; background: var(--white); }
  .search-icon { left: 776px; top: 6px; }

  /* Slider */
  .slider { left: 0; top: 179px; width: 850px; height: 333px; background: var(--white); }
  .slide-photo { left: 0; top: 0; width: 312px; height: 333px;
    background: linear-gradient(90deg, #b9c3c9 0%, #d8dee1 55%, #f4f5f6 90%, #ffffff 100%); }
  .slide-caption { left: 359px; top: 99px; font-family: Arial, Helvetica, sans-serif; font-size: 17px; color: var(--grey-text); }
  .slide-arrow { top: 150px; }
  .slide-arrow.prev { left: 31px; }
  .slide-arrow.next { left: 747px; }
  .slider-rail { left: 0; top: 512px; width: 850px; height: 21px;
    background: linear-gradient(#c9c9c9, #9a9a9a 50%, #7d7d7d); }

  /* About */
  .about { left: 0; top: 533px; width: 850px; height: 222px; }
  .section-title { font-size: 22px; font-weight: 700; letter-spacing: 0.6px; }
  .about .section-title { left: 93px; top: 28px; }
  .about-text { left: 93px; top: 65px; width: 430px; font-size: 15.2px; line-height: 19px; letter-spacing: 0.3px; }
  .button { display: flex; align-items: center; justify-content: center; background: linear-gradient(#1c1c1c, #050505);
    border-radius: 6px; border: 1px solid #000; box-shadow: 0 1px 0 rgba(255,255,255,0.15) inset; font-weight: 700; color: var(--white); }
  .read-more { left: 565px; top: 85px; width: 222px; height: 60px; font-size: 22px; letter-spacing: 1px; }

  /* Products */
  .catalogue { left: 0; top: 755px; width: 850px; height: 399px; }
  .catalogue .new-title { left: 93px; top: 32px; }
  .catalogue .products-title { left: 422px; top: 32px; }
  .divider { left: 387px; top: 31px; width: 2px; height: 341px; background: #b4b4b4; }
  .product { width: 105px; height: 94px; background: linear-gradient(160deg, #f2f2f2, #b8b8b8 60%, #8e8e8e); border: 2px solid var(--white); overflow: hidden; }
  .product span { position: absolute; left: 0; bottom: 0; width: 100%; height: 33px; line-height: 36px; text-align: center;
    background: rgba(70,70,70,0.85); font-size: 13.5px; letter-spacing: 0.3px; }
  .download-btn { left: 86px; top: 303px; width: 223px; height: 60px; font-size: 15.5px; letter-spacing: 0.6px; }
  .all-btn { left: 505px; top: 303px; width: 222px; height: 60px; font-size: 16.5px; letter-spacing: 0.8px; }

  .site-footer { left: 0; top: 1154px; width: 850px; height: 46px; background: var(--grey-dark);
    text-align: center; line-height: 46px; font-size: 13.5px; letter-spacing: 0.3px; }
</style>
</head>
<body>

<header class="site-header textured-blue abs">
  <div class="brand abs">
    <div class="brand-mark"></div>
    <span class="brand-name">Coldforge Prime</span>
  </div>
  <nav class="main-nav abs">
    <a href="#" style="left:0">Home</a>
    <a href="#" style="left:66px">About</a>
    <a href="#" style="left:134px">Products</a>
    <a href="#" style="left:226px">Download</a>
    <a href="#" style="left:329px">Contact</a>
  </nav>
</header>

<div class="utility-bar abs">
  <span class="utility-link abs">Download Catalogue</span>
  <div class="search-field abs"></div>
  <svg class="search-icon abs" width="9" height="9" viewBox="0 0 9 9">
    <circle cx="3.5" cy="3.5" r="2.4" fill="none" stroke="#fff" stroke-width="1.3"/>
    <line x1="5.2" y1="5.2" x2="8.2" y2="8.2" stroke="#fff" stroke-width="1.6"/>
  </svg>
</div>

<section class="slider abs">
  <div class="slide-photo abs" role="img" aria-label="Close-up of a stainless steel post with a glass panel clamp"></div>
  <p class="slide-caption abs">YOUR BEST CHOICE FOR RAILING SYSTEM</p>
  <svg class="slide-arrow prev abs" width="72" height="72" viewBox="0 0 72 72">
    <circle cx="36" cy="36" r="33" fill="#fff" stroke="#111" stroke-width="5"/>
    <polyline points="42,18 24,36 42,54" fill="none" stroke="#111" stroke-width="5"/>
  </svg>
  <svg class="slide-arrow next abs" width="72" height="72" viewBox="0 0 72 72">
    <circle cx="36" cy="36" r="33" fill="#fff" stroke="#111" stroke-width="5"/>
    <polyline points="30,18 48,36 30,54" fill="none" stroke="#111" stroke-width="5"/>
  </svg>
</section>

<ul class="dropdown abs">
  <li>Railing System</li>
  <li>Railing System</li>
  <li>Glass System</li>
  <li>Post &amp; Balustrade</li>
  <li>Accessories</li>
  <li>Square Tube Fitting</li>
  <li>Sliding Door &amp; Canpopy</li>
</ul>

<div class="slider-rail abs"></div>

<section class="about textured-blue abs">
  <h2 class="section-title abs">WHO WE ARE?</h2>
  <p class="about-text abs">Coldforge is always innovating to satisfy our customers by supplying solution of customer´s inquiry, supply a modular Railing system which is easy to use and competitively priced, develop, and design according to customer´s idea, supply Stainless Steel products</p>
  <a class="button read-more abs">READ MORE</a>
</section>

<section class="catalogue textured-grey abs">
  <h2 class="section-title new-title abs">WHAT’S NEW?</h2>
  <h2 class="section-title products-title abs">OUR PRODUCTS</h2>
  <div class="divider abs"></div>

  <div class="product abs" style="left:91px;top:85px" role="img" aria-label="Stainless glass clamp"><span>Product Name</span></div>
  <div class="product abs" style="left:204px;top:85px" role="img" aria-label="Stainless glass clamp"><span>Product Name</span></div>
  <div class="product abs" style="left:91px;top:192px" role="img" aria-label="Stainless glass clamp"><span>Product Name</span></div>
  <div class="product abs" style="left:204px;top:192px" role="img" aria-label="Stainless glass clamp"><span>Product Name</span></div>

  <div class="product abs" style="left:423px;top:85px" role="img" aria-label="Stainless glass clamp"><span>Product Name</span></div>
  <div class="product abs" style="left:552px;top:85px" role="img" aria-label="Stainless glass clamp"><span>Product Name</span></div>
  <div class="product abs" style="left:679px;top:85px" role="img" aria-label="Stainless glass clamp"><span>Product Name</span></div>
  <div class="product abs" style="left:423px;top:192px" role="img" aria-label="Stainless glass clamp"><span>Product Name</span></div>
  <div class="product abs" style="left:552px;top:192px" role="img" aria-label="Stainless glass clamp"><span>Product Name</span></div>
  <div class="product abs" style="left:679px;top:192px" role="img" aria-label="Stainless glass clamp"><span>Product Name</span></div>

  <a class="button download-btn abs">DOWNLOAD CATALOGUE</a>
  <a class="button all-btn abs">CHECK ALL PRODUCTS</a>
</section>

<footer class="site-footer abs">Copyright © Company Name. All Rights Reserved.</footer>

</body>
</html>
```